Plakat-Design für Veltramo
Zielgruppe
Wir sind eine 'kreative' kleine Truppe, die mit neuen Ideen versuchen wollen, auch mal andere Wege in den Projekten zu gehen.
Aufgabenstellung
Für die Motivation meiner Mitarbeiter und für meinen Empfang suche ich Plakate in der Höhe von ca. 150 cm und Breite von etwa 50 cm.
Sie sollen die weißen Wände etwas auflockern, von daher hätte ich gern die Hauptfarbe im Hintergrund. Ansonsten bitte für die Farbakzente die CD-Farben nutzen.
Grundsätzlich soll das Thema "Einfach Machen" sein. Ich möchte damit animieren Dinge und Wege auszuprobieren, ohne vorab immer scheu davor zu haben.
Gerne auch mit weiteren Textvorschlägen. Pro neuen Text, der dann auf ein Poster kommt, zahle ich einen Bonus von 40€.

```html
<!DOCTYPE html>
<html lang="de">
<head>
<meta charset="utf-8">
<title>Veltramo – Einfach machen</title>
<link href="https://fonts.googleapis.com/css2?family=Barlow:wght@400;500;600;700&display=swap" rel="stylesheet">
<style>
  :root {
    --bg: #434b4e;
    --accent-green: #96d3b0;
    --text-grey: #bab9be;
    --brand-light: #dfe3e6;
  }
  html, body {
    margin: 0;
    padding: 0;
    overflow: hidden;
  }
  .poster {
    position: relative;
    width: 1200px;
    height: 3598px;
    background: var(--bg);
    font-family: "Barlow", "DIN Alternate", Arial, sans-serif;
    overflow: hidden;
  }
  .headline {
    position: absolute;
    top: 566px;
    left: 0;
    width: 100%;
    margin: 0;
    text-align: center;
    color: var(--accent-green);
    font-weight: 700;
    font-size: 230px;
    line-height: 244px;
    letter-spacing: 0.1em;
    text-indent: 0.1em;
    text-transform: uppercase;
  }
  .headline span { display: block; }
  .quote {
    position: absolute;
    top: 1368px;
    left: 0;
    width: 100%;
    margin: 0;
    text-align: center;
    color: var(--text-grey);
    font-weight: 600;
    font-size: 80px;
    line-height: 113px;
    letter-spacing: 0.02em;
    text-transform: uppercase;
  }
  .quote span { display: block; }
  .tagline {
    position: absolute;
    top: 3142px;
    left: 0;
    width: 100%;
    margin: 0;
    text-align: center;
    color: var(--text-grey);
    font-weight: 400;
    font-size: 56px;
    line-height: 1;
    letter-spacing: 0.02em;
    text-transform: uppercase;
  }
  .brand-name {
    position: absolute;
    top: 3275px;
    left: 0;
    width: 100%;
    margin: 0;
    text-align: center;
    color: var(--brand-light);
    font-weight: 500;
    font-size: 170px;
    line-height: 1;
    letter-spacing: 0.01em;
  }
</style>
</head>
<body>
  <main class="poster">
    <h1 class="headline">
      <span>Mach‘s</span>
      <span>Einfach</span>
      <span>Machen</span>
    </h1>
    <p class="quote">
      <span>Du bist ein Genie,</span>
      <span>wenn du im Ende</span>
      <span>auch immer einen</span>
      <span>Anfang erkennst.</span>
    </p>
    <p class="tagline">Einfach machen!</p>
    <p class="brand-name">Veltramo</p>
  </main>
</body>
</html>
```